"Client Services Packet" Folder design for Hair Tissue Mineral Analysis Company

We are looking for an updated folder design which we use mail our new clients information and starter kits for our services. We are looking for a clean and simple design to match our new logo. We would like our logo along with "Client Services Packet" on the front cover with our company information located inside the folder.
Logo file and color palette will be uploaded in the brief.
**Folder will not need the business card cutout shown on current folder**
Address:
4718 E. Torvin Street
Phoenix, AZ 85021
Phone:
1-602-447-3916
1-800-739-2185
Fax:
1-602-864-5207
Website:
www.quvesko.com
Email:
information@quvesko.com

```html
<!DOCTYPE html>
<html lang="en">
<head>
<meta charset="utf-8">
<title>Client Services Packet Folder</title>
<link href="https://fonts.googleapis.com/css2?family=Poppins:wght@400;600;700&display=swap" rel="stylesheet">
<style>
  :root {
    --backdrop: #b3b3b3;
    --navy: #0b1835;
    --orange: #f38426;
    --paper: #f1f1f3;
    --blue: #2c5ba6;
    --white: #ffffff;
  }
  html, body {
    margin: 0;
    padding: 0;
    overflow: hidden;
  }
  .canvas {
    position: relative;
    width: 1190px;
    height: 1200px;
    background: var(--backdrop);
    overflow: hidden;
    font-family: "Poppins", sans-serif;
  }
  .folder-shapes {
    position: absolute;
    inset: 0;
  }
  .brand {
    position: absolute;
    top: 340px;
    display: flex;
    align-items: center;
    gap: 8px;
    font-family: "Poppins", sans-serif;
    font-weight: 600;
    font-size: 25px;
    letter-spacing: 1px;
    color: var(--blue);
    line-height: 1;
  }
  .brand-dot {
    width: 12px;
    height: 12px;
    border-radius: 50%;
    background: var(--orange);
  }
  .brand--back { left: 203px; }
  .brand--front { left: 652px; }
  .title {
    position: absolute;
    margin: 0;
    font-family: "Poppins", sans-serif;
    font-weight: 700;
    font-size: 41px;
    line-height: 40.5px;
    letter-spacing: 0.3px;
  }
  .title span { display: block; }
  .title--back { left: 201px; top: 469px; color: var(--white); }
  .title--back .accent { color: var(--orange); }
  .title--front { left: 650px; top: 593px; }
  .title--front .line-1 { color: var(--orange); }
  .title--front .line-2 { color: var(--navy); }
  .title--front .line-3 { color: var(--blue); }
  .contact-list {
    position: absolute;
    left: 203px;
    top: 680px;
    margin: 0;
    padding: 0;
    list-style: none;
    color: var(--white);
    font-size: 10.5px;
    letter-spacing: 0.2px;
  }
  .contact-list li {
    display: flex;
    align-items: center;
    height: 20px;
    margin-bottom: 4.6px;
  }
  .contact-list li.address { margin-top: 3px; }
  .contact-icon {
    width: 13px;
    height: 13px;
    margin-right: 11px;
    flex: none;
  }
</style>
</head>
<body>
<div class="canvas">
  <svg class="folder-shapes" width="1190" height="1200" viewBox="0 0 1190 1200" aria-hidden="true">
    <!-- pocket and tab -->
    <rect class="tab" x="134" y="637" width="40" height="204" rx="26" fill="var(--orange)"/>
    <polygon class="pocket" points="159,841 618,841 552,1045 159,1045" fill="var(--orange)"/>
    <!-- back panel -->
    <rect class="back-panel" x="159" y="229" width="459" height="612" fill="var(--navy)"/>
    <!-- front panel -->
    <rect class="front-panel" x="618" y="229" width="461" height="612" fill="var(--navy)"/>
    <path class="front-wave-accent" d="M618,229 H980 C928,290 932,400 979,478 C1012,540 1024,600 1024,648 C1024,770 985,841 935,841 H618 Z" fill="var(--orange)"/>
    <path class="front-wave" d="M618,229 H952 C906,290 904,400 979,478 C1010,540 1024,600 1024,648 C1024,762 968,841 900,841 H618 Z" fill="var(--paper)"/>
  </svg>

  <div class="brand brand--back"><span class="brand-dot"></span>QUVESKO LABS</div>
  <div class="brand brand--front"><span class="brand-dot"></span>QUVESKO LABS</div>

  <h1 class="title title--back">
    <span>CLIENT</span>
    <span class="accent">SERVICES</span>
    <span>PACKET</span>
  </h1>

  <h2 class="title title--front">
    <span class="line-1">CLIENT</span>
    <span class="line-2">SERVICES</span>
    <span class="line-3">PACKET</span>
  </h2>

  <ul class="contact-list">
    <li class="fax">
      <svg class="contact-icon" viewBox="0 0 16 16" fill="none" stroke="var(--orange)" stroke-width="1.2"><rect x="1" y="4" width="4" height="11" rx="1"/><rect x="5" y="5" width="10" height="10" rx="1"/><rect x="7" y="1" width="6" height="4"/><path d="M8 8h1M11 8h1M8 10.5h1M11 10.5h1M8 13h1M11 13h1"/></svg>
      1-602-864-5207
    </li>
    <li class="phone">
      <svg class="contact-icon" viewBox="0 0 16 16" fill="var(--orange)"><path d="M3.2 1.2l2.3-.4 1.6 3.6-1.5 1.3c.8 1.9 2.3 3.4 4.2 4.2l1.3-1.5 3.6 1.6-.4 2.3c-.2.9-1 1.5-1.9 1.4C6.6 13.2 2.6 9.2 1.8 3.1c-.1-.9.5-1.7 1.4-1.9z"/></svg>
      1-602-447-3916&nbsp;&nbsp;||&nbsp;&nbsp;1-800-739-2185
    </li>
    <li class="email">
      <svg class="contact-icon" viewBox="0 0 16 16" fill="none" stroke="var(--orange)" stroke-width="1.4"><rect x="1" y="3" width="14" height="10"/><path d="M1 3l7 6 7-6M1 13l5-5M15 13l-5-5"/></svg>
      information@quvesko.com
    </li>
    <li class="web">
      <svg class="contact-icon" viewBox="0 0 16 16" fill="none" stroke="var(--orange)" stroke-width="1.3"><circle cx="8" cy="8" r="6.8"/><ellipse cx="8" cy="8" rx="3" ry="6.8"/><path d="M1.2 8h13.6M2.2 4.6h11.6M2.2 11.4h11.6"/></svg>
      www.quvesko.com
    </li>
    <li class="address">
      <svg class="contact-icon" viewBox="0 0 16 16" fill="var(--orange)"><path d="M8 .5a5.5 5.5 0 0 0-5.5 5.5c0 4 5.5 9.5 5.5 9.5s5.5-5.5 5.5-9.5A5.5 5.5 0 0 0 8 .5zm0 7.8a2.2 2.2 0 1 1 0-4.4 2.2 2.2 0 0 1 0 4.4z"/></svg>
      4718 E. Torvin Street Phoenix, AZ 85021
    </li>
  </ul>
</div>
</body>
</html>
```